New Email Marketing Design Project

I’d like you to make an email template. I’ll be welcoming and on boarding customers via email. And I’d like the branding to stand out. Keep it professional and simple. But be creative.

Design should look amazing on desktop and mobile phones.

Negative white space is ok.

Use stock images

I’ll like to have a spot for a picture of myself so make sure to include a circle where I can show my face so that email viewers will know who is speaking to them.

Target Market(s)

Practice managers, doctors, medical providers

Font styles to use
Sans Serif

Requirements
Must have
• Our Logo, CTA buttons, Same colors as website.
https://www.tavrenhealthclaims.com

```html
<!DOCTYPE html>
<html lang="en">
<head>
<meta charset="utf-8">
<title>Tavren Health Claims — Welcome Email</title>
<link rel="stylesheet" href="https://fonts.googleapis.com/css2?family=Poppins:wght@400;500;600&family=Open+Sans:wght@400;600&family=Libre+Baskerville&family=Roboto:wght@500;700&display=swap">
<style>
  :root{
    --navy:#03456a;
    --teal:#2f7a9e;
    --ink:#1d4257;
    --body:#444b50;
    --page:#f2f5f8;
    --topbar:#c8cfd2;
    --tile-bg:#f4f4f4;
    --white:#ffffff;
    --line:#cdd7df;
  }
  *{margin:0;padding:0;box-sizing:border-box}
  html,body{width:1200px;height:2322px;overflow:hidden}
  body{position:relative;background:var(--page);font-family:"Open Sans",Arial,sans-serif;color:var(--body)}
  .abs{position:absolute}
  .center{left:0;width:100%;text-align:center}

  .browser-bar{top:0;left:0;width:1200px;height:75px;background:var(--topbar);display:flex;align-items:center;justify-content:center;font-family:Arial,Helvetica,sans-serif;font-size:21px;color:#555}
  .brand-header{top:75px;left:0;width:1200px;height:181px;background:var(--page)}
  .brand-mark{left:247px;top:97px;width:138px;height:138px;border-radius:50%;background:var(--teal)}
  .brand-name{left:417px;top:134px;font-family:"Poppins",sans-serif;font-weight:500;font-size:37px;letter-spacing:1px;color:var(--teal)}

  .hero-band{top:256px;left:0;width:1200px;height:437px;background:var(--navy)}
  .hero-greeting{top:334px;font-family:"Libre Baskerville",Georgia,serif;font-weight:400;font-size:96px;color:var(--white);line-height:1.1}

  .email-card{top:475px;left:178px;width:841px;height:1472px;background:var(--white)}
  .card-title{font-family:"Poppins",sans-serif;font-weight:600;color:var(--navy)}
  .welcome-title{top:522px;font-size:52px;letter-spacing:1px}
  .card-text{font-size:22px;line-height:39px;color:var(--body)}
  .welcome-text{top:614px}
  .btn{display:flex;align-items:center;justify-content:center;color:var(--white);font-family:"Open Sans",sans-serif;font-size:22px;background:var(--teal)}
  .btn-explore{left:460px;top:718px;width:279px;height:75px}
  .card-divider{left:178px;top:838px;width:841px;height:2px;background:#e6e9eb}
  .about-title{top:875px;font-size:37px;font-weight:500}
  .about-text{top:965px}
  .services-title{top:1075px;font-size:38px;font-weight:500}

  .services-panel{left:178px;top:1156px;width:841px;height:456px;background:var(--tile-bg)}
  .service-tile{width:187px;height:148px;background:var(--white);box-shadow:0 1px 4px rgba(0,0,0,.12);display:flex;flex-direction:column;align-items:center;padding-top:20px}
  .service-tile svg{width:56px;height:56px}
  .service-label{margin-top:14px;font-family:"Roboto",Arial,sans-serif;font-weight:700;font-size:13.5px;line-height:18px;color:#111;text-align:center;text-transform:uppercase}
  .btn-browse{left:465px;top:1519px;width:273px;height:57px}

  .sender-photo{left:210px;top:1652px;width:250px;height:250px;border-radius:50%;border:5px solid #f3f3f3;background:linear-gradient(135deg,#e8edf0 0%,#c9d2d8 45%,#24324a 70%,#1b2640 100%)}
  .sender-thanks{left:508px;top:1677px;font-family:"Open Sans",sans-serif;font-size:25px;font-weight:600;color:var(--ink)}
  .sender-name{left:506px;top:1712px;font-family:"Poppins",sans-serif;font-size:38px;font-weight:500;color:var(--ink)}
  .sender-role{left:508px;top:1775px;font-family:"Poppins",sans-serif;font-size:23px;font-weight:600;color:var(--ink)}
  .btn-help{left:507px;top:1834px;width:339px;height:57px;background:var(--ink)}

  .contact-footer{left:0;top:1948px;width:1200px;height:213px;background:var(--white);border:3px solid var(--line);font-family:"Poppins",sans-serif;font-size:22px;color:var(--ink)}
  .contact-footer p{position:absolute;left:0;width:100%;text-align:center}
  .contact-footer b{font-weight:600}
  .social-row{left:0;top:2187px;width:1200px;height:74px}
  .social-link{position:absolute;top:0;width:74px;height:74px;border:3px solid var(--ink);border-radius:50%}
</style>
</head>
<body>
  <div class="abs browser-bar">Don’t see this email properly? View in web browser</div>

  <header class="abs brand-header"></header>
  <div class="abs brand-mark" role="img" aria-label="Tavren Health Claims mark"></div>
  <div class="abs brand-name">Tavren Health Claims</div>

  <section class="abs hero-band"></section>
  <h1 class="abs center hero-greeting">Hi!</h1>

  <main class="abs email-card"></main>
  <h2 class="abs center card-title welcome-title">WELCOME!</h2>
  <p class="abs center card-text welcome-text">We’re exicitied to have you get started. Please feel easy and<br>browse our services.</p>
  <a class="abs btn btn-explore">Explore Our services</a>
  <div class="abs card-divider"></div>

  <h2 class="abs center card-title about-title">About Us</h2>
  <p class="abs center card-text about-text">Tavren Health Claims will allow you to save on overhead expenses<br>such as salaries, payroll taxes, benefits, and printing/office supplies.</p>
  <h2 class="abs center card-title services-title">Services Highlight</h2>

  <section class="abs services-panel"></section>

  <div class="abs service-tile" style="left:193px;top:1177px">
    <svg viewBox="0 0 56 56" fill="none" stroke="#2f7a9e" stroke-width="2"><circle cx="18" cy="18" r="7"/><rect x="26" y="10" width="22" height="26" rx="2"/><path d="M8 46c0-8 5-14 10-14s10 6 10 14"/><path d="M31 18h12M31 24h12M31 30h8"/></svg>
    <span class="service-label">Clearinghouse<br>Maintenance</span>
  </div>
  <div class="abs service-tile" style="left:402px;top:1177px">
    <svg viewBox="0 0 56 56" fill="none" stroke="#2f7a9e" stroke-width="2"><rect x="12" y="6" width="28" height="42" rx="2"/><path d="M18 16h16M18 22h16M18 28h10"/><circle cx="40" cy="36" r="8"/><path d="M40 32v8M36 36h8"/></svg>
    <span class="service-label">Medical Billing</span>
  </div>
  <div class="abs service-tile" style="left:611px;top:1177px">
    <svg viewBox="0 0 56 56" fill="none" stroke="#2f7a9e" stroke-width="2"><rect x="8" y="6" width="12" height="16"/><rect x="22" y="6" width="12" height="16"/><rect x="36" y="6" width="12" height="16"/><path d="M28 26v8M10 40l18-8 18 8-18 8z"/></svg>
    <span class="service-label">Patient Collections</span>
  </div>
  <div class="abs service-tile" style="left:819px;top:1177px">
    <svg viewBox="0 0 56 56" fill="none" stroke="#2f7a9e" stroke-width="2"><path d="M12 6h20l10 10v32H12z"/><path d="M18 22l6 4 8-10"/><circle cx="40" cy="36" r="5"/><path d="M32 50c0-5 4-8 8-8s8 3 8 8"/></svg>
    <span class="service-label">Insurance<br>Credentialing</span>
  </div>

  <div class="abs service-tile" style="left:193px;top:1344px">
    <svg viewBox="0 0 56 56" fill="none" stroke="#2f7a9e" stroke-width="2"><rect x="10" y="8" width="14" height="18"/><path d="M14 14h6M14 20h6"/><rect x="6" y="30" width="44" height="16" rx="2"/><path d="M30 8l16 16M46 8 30 24"/></svg>
    <span class="service-label">Claim Denial</span>
  </div>
  <div class="abs service-tile" style="left:402px;top:1344px">
    <svg viewBox="0 0 56 56" fill="none" stroke="#2f7a9e" stroke-width="2"><rect x="10" y="6" width="28" height="42" rx="2"/><rect x="15" y="11" width="18" height="8"/><path d="M15 26h18M15 32h18M15 38h10"/><circle cx="40" cy="40" r="7"/><path d="M37 43l6-6"/></svg>
    <span class="service-label">Claim Appeals</span>
  </div>
  <div class="abs service-tile" style="left:611px;top:1344px">
    <svg viewBox="0 0 56 56" fill="none" stroke="#2f7a9e" stroke-width="2"><rect x="14" y="4" width="28" height="48" rx="4"/><path d="M20 14h16M20 20h16M20 26h10M20 38h16"/><circle cx="28" cy="46" r="1.5"/></svg>
    <span class="service-label">EDI Claim Submission<br>Setup</span>
  </div>
  <div class="abs service-tile" style="left:819px;top:1344px">
    <svg viewBox="0 0 56 56" fill="none" stroke="#2f7a9e" stroke-width="2"><circle cx="28" cy="28" r="22"/><circle cx="28" cy="28" r="17"/><path d="M28 16v22M20 30l8 8 8-8"/></svg>
    <span class="service-label">Electronic Claim<br>Submission</span>
  </div>

  <a class="abs btn btn-browse">Browse More Services</a>

  <div class="abs sender-photo" role="img" aria-label="Circular portrait photo of the company CEO"></div>
  <p class="abs sender-thanks">Thanks &amp; Regards</p>
  <p class="abs sender-name">Daniel Hart</p>
  <p class="abs sender-role">CEO, Tavren Health Claims</p>
  <a class="abs btn btn-help">Need More Help? Click Here</a>

  <footer class="abs contact-footer">
    <p style="top:46px"><b>Phone:</b> 555-014-0110 &nbsp;&nbsp;|&nbsp;&nbsp; <b>Fax:</b> 555-014-0110</p>
    <p style="top:91px"><b>Email:</b> hello@tavrenhealthclaims.com</p>
    <p style="top:139px">210 Harbor Ave Ste 400, Fairview, Minnesota 55000</p>
  </footer>

  <nav class="abs social-row" aria-label="Social links">
    <a class="social-link" style="left:417px" aria-label="Social profile 1"></a>
    <a class="social-link" style="left:518px" aria-label="Social profile 2"></a>
    <a class="social-link" style="left:611px" aria-label="Social profile 3"></a>
    <a class="social-link" style="left:701px" aria-label="Social profile 4"></a>
  </nav>
</body>
</html>
```